Live at Velmora Playhouse Recital Series

Velmora Playhouse Recital Series

Febraury 1st - Peter Dale Farnsby (Quill Winner, Harbor Kids)
March 1st - Celia Vantrose (Silver Lantern Winner, The Fern)
April 5th - Dorothy Pell (A Tribute to Nora: The First Decade)
May 3rd - Beatrix Solvane (Quill Nominee, Mabel)

All shows at 7:30PM

Subscribe to the series and save 10%

Get your tickets online at www.velkastagehouses.com

Poster size 11" X 17" also 27" x 41"

Target Market(s)

Upscale market and music lovers. Small venue with international performers

Colors

Designer to choose colors to be used in the design.

Requirements
Must have
• Upscale - rich - style - like DIVA
Should not have
• Clip art

```html
<!DOCTYPE html>
<html lang="en">
<head>
<meta charset="utf-8">
<title>Velmora Playhouse Recital Series</title>
<link rel="stylesheet" href="https://fonts.googleapis.com/css2?family=Questrial&family=Raleway:wght@400;500&family=Arimo:wght@400;700&display=swap">
<style>
  :root {
    --stage-red: #c8101c;
    --deep-red: #5a0308;
    --night: #0d0204;
    --gold: #f5ea1e;
    --white: #ffffff;
    --ink: #000000;
    --ticket-red: #e0231c;
  }
  * { margin: 0; padding: 0; box-sizing: border-box; }
  html, body { width: 776px; height: 1200px; overflow: hidden; background: var(--night); }
  .poster {
    position: relative; width: 776px; height: 1200px; overflow: hidden;
    background:
      radial-gradient(ellipse 520px 420px at 440px 40px, rgba(230,30,40,.95), rgba(180,10,20,.7) 45%, rgba(90,5,12,0) 80%),
      radial-gradient(ellipse 420px 520px at 420px 820px, rgba(70,60,90,.45), rgba(0,0,0,0) 70%),
      linear-gradient(180deg, var(--deep-red) 0%, #2a0206 45%, var(--night) 100%);
    font-family: "Arimo", Arial, sans-serif;
  }
  .stage-rays { position: absolute; inset: 0; width: 776px; height: 700px; }
  .portrait {
    position: absolute; background: var(--white); padding: 7px;
    box-shadow: 0 6px 18px rgba(0,0,0,.6);
  }
  .portrait .photo { width: 100%; height: 100%; }
  .portrait-farnsby { left: 27px; top: 148px; width: 208px; height: 292px; transform: rotate(-6deg); }
  .portrait-farnsby .photo { background: linear-gradient(160deg, #eae6e4, #c9c2bf); }
  .portrait-vantrose { left: 195px; top: 387px; width: 176px; height: 276px; transform: rotate(3deg); z-index: 2; }
  .portrait-vantrose .photo { background: linear-gradient(170deg, #6e6c6e, #1d1b1e); }
  .portrait-pell { left: 24px; top: 496px; width: 195px; height: 316px; transform: rotate(-6deg); z-index: 1; }
  .portrait-pell .photo { background: linear-gradient(165deg, #b0232a, #3a2520 70%); }
  .portrait-solvane { left: 140px; top: 708px; width: 223px; height: 302px; transform: rotate(5deg); z-index: 3; }
  .portrait-solvane .photo { background: linear-gradient(160deg, #f0e6ea, #b86a4a 60%, #2a1a1a); }

  .title { position: absolute; left: 240px; top: 188px; width: 520px; text-align: center; color: var(--white); }
  .title-name { font-family: "Questrial", sans-serif; font-size: 92px; line-height: 1; letter-spacing: 1px; font-weight: 400; }
  .title-sub { font-family: "Raleway", sans-serif; font-size: 41px; margin-top: 6px; font-weight: 400; }

  .schedule { position: absolute; left: 420px; width: 320px; top: 436px; text-align: center; color: var(--white); }
  .show { margin-bottom: 14px; }
  .show-date { color: var(--gold); font-weight: 700; font-size: 30px; line-height: 36px; }
  .show-artist { font-weight: 700; font-size: 24px; line-height: 30px; }
  .show-note { font-size: 18px; line-height: 24px; white-space: nowrap; margin-left: -30px; margin-right: -30px; }
  .showtime { font-weight: 700; font-size: 24px; margin-top: 10px; }

  .on-sale {
    position: absolute; left: 243px; top: 1062px; width: 288px; height: 36px;
    background: rgba(20,0,0,.85); color: var(--ticket-red);
    font-size: 24px; line-height: 36px; text-align: center;
  }
  .footer { position: absolute; left: 0; top: 1100px; width: 776px; height: 100px; background: var(--ink); text-align: center; }
  .footer-offer { color: var(--white); font-weight: 700; font-size: 23px; padding-top: 14px; }
  .footer-web { color: var(--gold); font-size: 22px; margin-top: 8px; }
</style>
</head>
<body>
<main class="poster">
  <svg class="stage-rays" viewBox="0 0 776 700" aria-hidden="true">
    <defs>
      <linearGradient id="ray" x1="0" y1="0" x2="0" y2="1">
        <stop offset="0" stop-color="#ff4a52" stop-opacity=".35"/>
        <stop offset="1" stop-color="#ff4a52" stop-opacity="0"/>
      </linearGradient>
    </defs>
    <polygon points="430,0 470,0 620,600 520,600" fill="url(#ray)"/>
    <polygon points="380,0 410,0 340,620 240,620" fill="url(#ray)"/>
    <polygon points="480,0 505,0 760,420 700,470" fill="url(#ray)"/>
    <polygon points="350,0 372,0 60,420 10,380" fill="url(#ray)"/>
  </svg>

  <figure class="portrait portrait-farnsby"><div class="photo" role="img" aria-label="Portrait of Peter Dale Farnsby"></div></figure>
  <figure class="portrait portrait-pell"><div class="photo" role="img" aria-label="Portrait of Dorothy Pell"></div></figure>
  <figure class="portrait portrait-vantrose"><div class="photo" role="img" aria-label="Portrait of Celia Vantrose"></div></figure>
  <figure class="portrait portrait-solvane"><div class="photo" role="img" aria-label="Portrait of Beatrix Solvane"></div></figure>

  <header class="title">
    <h1 class="title-name">VELMORA</h1>
    <p class="title-sub">Playhouse Recital Series</p>
  </header>

  <section class="schedule">
    <div class="show">
      <p class="show-date">February 1st</p>
      <p class="show-artist">Peter Dale Farnsby</p>
      <p class="show-note">(Quill Winner, Harbor Kids)</p>
    </div>
    <div class="show">
      <p class="show-date">March 1st</p>
      <p class="show-artist">Celia Vantrose</p>
      <p class="show-note">(Silver Lantern Winner, The Fern)</p>
    </div>
    <div class="show">
      <p class="show-date">April 5th</p>
      <p class="show-artist">Dorothy Pell</p>
      <p class="show-note">(A Tribute to Nora: The First Decade)</p>
    </div>
    <div class="show">
      <p class="show-date">May 3rd</p>
      <p class="show-artist">Beatrix Solvane</p>
      <p class="show-note">(Quill Nominee, Mabel)</p>
    </div>
    <p class="showtime">All shows at 7:30PM</p>
  </section>

  <p class="on-sale">TICKETS ON SALE NOW!</p>

  <footer class="footer">
    <p class="footer-offer">Subscribe to the series and save 10%</p>
    <p class="footer-web">Get your tickets online at&nbsp; www.velkastagehouses.com</p>
  </footer>
</main>
</body>
</html>
```